Email Signature

We are looking for creative email signature for our company. Please find attached the logo of our company for your reference. now we understand there isn't much can be done with email signature but we are looking for out of the box designs. Nothing specific in mind

Please insert fake numbers, website and/or address, etc just to showcase the designs. once the design is chosen we will provide the actual details.
Updates

Dear All,

We wouldlike to extend our apology for not being able to provide feedbacks to everysingle design. We were extremely busy and we have multiple contests opensimultaneously which makes the process harder. However, thank you all for theefforts you have put into this contest. We have received anoverwhelming quality responses & it has been a very difficult task tochoose just one, we easily Loved at least several designs...

Thanksagain for participating, we wish you all success in your design ventures.

Kindregards,

HLW Team

Industry/Entity Type

It Company

```html
<!DOCTYPE html>
<html lang="en">
<head>
<meta charset="utf-8">
<title>Harbor Lantern – Email Signature</title>
<link href="https://fonts.googleapis.com/css2?family=Source+Sans+3:wght@400;700&display=swap" rel="stylesheet">
<style>
  :root {
    --brand-blue: #1283dc;
    --icon-blue: #1a7fd0;
    --brand-green: #7dc242;
    --ink: #2b2b2b;
    --paper: #ffffff;
    --rule: #d6d6d6;
  }
  * { margin: 0; padding: 0; box-sizing: border-box; }
  html, body { width: 1200px; height: 444px; overflow: hidden; background: var(--paper); }
  body { font-family: "Source Sans 3", sans-serif; color: var(--ink); }

  .signature { position: relative; width: 1200px; height: 444px; background: var(--paper); }

  .top-band { position: absolute; left: 0; top: 0; width: 100%; height: 137px; background: var(--brand-blue); }
  .accent-line { position: absolute; left: 0; top: 140px; width: 100%; height: 5px; background: var(--brand-green); }

  .brand-mark {
    position: absolute; left: 300px; top: 74px; width: 600px; height: 128px;
    background: var(--paper); border-radius: 22px;
    display: flex; align-items: center; justify-content: center;
  }
  .brand-name {
    font-weight: 700; font-size: 74px; line-height: 1; letter-spacing: -1px;
    color: var(--brand-blue);
  }

  .identity {
    position: absolute; right: calc(1200px - 573px); top: 282px;
    text-align: right;
  }
  .person-name { font-weight: 700; font-size: 29px; line-height: 34px; color: var(--brand-blue); }
  .person-title { font-size: 22px; line-height: 28px; margin-bottom: 8px; }
  .address-line { font-size: 22px; line-height: 31px; }

  .divider { position: absolute; left: 597px; top: 276px; width: 1px; height: 140px; background: var(--rule); }

  .contacts { position: absolute; left: 619px; top: 284px; list-style: none; }
  .contact-item { display: flex; align-items: center; height: 46px; font-size: 23px; }
  .contact-icon { width: 22px; height: 22px; margin-right: 11px; flex: none; }
</style>
</head>
<body>
  <main class="signature">
    <div class="top-band"></div>
    <div class="accent-line"></div>

    <div class="brand-mark">
      <span class="brand-name">Harbor Lantern</span>
    </div>

    <section class="identity">
      <p class="person-name">Your Name</p>
      <p class="person-title">Title</p>
      <p class="address-line">Door No.,Street Name</p>
      <p class="address-line">City Name, State Zip Code</p>
    </section>

    <div class="divider"></div>

    <ul class="contacts">
      <li class="contact-item">
        <svg class="contact-icon" viewBox="0 0 24 24" aria-hidden="true">
          <circle cx="12" cy="12" r="10.5" fill="none" stroke="var(--icon-blue)" stroke-width="1.6"/>
          <path d="M9 6.5c-1.6 1-2 2.6-1.3 4.6.9 2.6 2.8 5 5.2 6.3 1.7.9 3 .6 3.9-.6l-2-2-1.5.9c-1.4-.8-2.5-2.2-3.1-3.7l1.3-1.1L9 6.5z" fill="var(--icon-blue)"/>
        </svg>
        <span>123-456-7890</span>
      </li>
      <li class="contact-item">
        <svg class="contact-icon" viewBox="0 0 24 24" aria-hidden="true">
          <rect x="7" y="3" width="10" height="6" fill="var(--icon-blue)"/>
          <rect x="2" y="9" width="20" height="9" rx="2" fill="var(--icon-blue)"/>
          <rect x="6" y="14" width="12" height="7" fill="var(--icon-blue)" stroke="#fff" stroke-width="1"/>
        </svg>
        <span>123-456-7890</span>
      </li>
      <li class="contact-item">
        <svg class="contact-icon" viewBox="0 0 24 24" aria-hidden="true">
          <circle cx="12" cy="12" r="10" fill="var(--icon-blue)"/>
          <g fill="none" stroke="#fff" stroke-width="1.2">
            <ellipse cx="12" cy="12" rx="4.5" ry="10"/>
            <line x1="2" y1="12" x2="22" y2="12"/>
            <line x1="12" y1="2" x2="12" y2="22"/>
            <path d="M4 7h16M4 17h16"/>
          </g>
        </svg>
        <span>www.harborlantern.com</span>
      </li>
    </ul>
  </main>
</body>
</html>
```